依頼詳細
■サイトマップ
①ホーム
②〇〇について
③教室紹介
④講師紹介(一覧)
⑤講師紹介(詳細)
⑥時間割(一覧)
⑦小学生の方へ(Q&A集)
⑧中学生の方へ(Q&A集)
⑨中学受験をお考えの方
⑩高校受験をお考えの方
⑪合格実績(一覧)
⑫合格体験記(一覧)
⑬合格体験記(詳細)
⑭コラム(一覧)
⑮コラム(詳細)
⑯新着情報(一覧)
⑰新着情報(詳細)
⑱お問い合わせ

■希望デザインカラー
緑系(健康・ナチュラル)
黄色・オレンジ(ポップ・にぎやか)

彩度・明度
ソフト  ストロング

■参考サイト
https://malvinu.co.jp/recruit/
https://tolk-morrow.net/
https://www.ves-academy.jp/

■フォントについて
・無料で使えるフォントで作成お願い致します
・OSに紐づくフォントの使用は控えていただければと思います (ミズセラなど)

■文章について
・現行ホームページに記載しているテキストを使用して下さい。
・可能な限り「ダミーテキスト」を繰り返した文字の配置は避けてください。

■制作要望・素材・ロゴ・サイトマップについて
・下記よりダウンロードしてご使用ください
URL:https://filebunko.jp/download/7a3c91fe20bd8e4471c05a9d3e6b82f0ad19c7e2
パスワード:58316094

・また、現行サイトの素材や内容を使用頂いても問題ありません。
サイトURL
http://www.kelvado.jp/
ページ数
1ページ
希望イメージ
シンプル 複雑
単色 カラフル
暗い 明るい
日常 高級
遊び心 厳粛
未来的 伝統的
女性的 男性的
希望する色
緑系、黄・オレンジ系
納品ファイル
• イラストレーター形式 (.ai)
• フォトショップ形式 (.psd)
補足説明
■写真について
・Pixaro Bank( https://bank.pixaro.com/jp/ )で定期契約をしています
また定期契約のものは弊社の負担となり、ランサー様に負担はありません。
・カンプ画像を入れてください
その際、通常アセットで購入できる画像でお願いいたします。

■その他
・業務への支障がでる可能性がございますので、店舗への直接の連絡はお控え下さい
・申し訳ございませんがXD形式の納品はお受けできかねます。
・デザインの横幅は1300pxで作成お願いいたします。
・有料フォントの使用はしないようにしてください。
様々なバリエーションから検討させていただきたく、期限延長いたします。
皆様日頃よりご提案くださりありがとうございます。
期間を延長し、様々なバリエーションより選定させていただきたく存じます。
何卒引き続き宜しくお願い申し上げます。
依頼金額を36300円に変更して、延長しました。
様々なパターンより選定させていただきたく、この度延長いたします。
スタッフ写真に関しては現行サイトにカラー版がありますのでご認識下さい。
引き続きよろしくお願いいたします。
皆様ご提案くださりありがとうございます。
良いデザインが集まってきており嬉しい限りでございます。
期限を延長し更にバリエーションを増やして検討したく存じます。
引き続きご協力の程、何卒宜しくお願い申し上げます。
皆様お世話になっております。
期限いっぱいまで延長し募ってまいりますので、引き続きよろしくお願いいたします。
ご自身のブラッシュアップしたデザインでも結構ですので
様々なパターンを拝見したく存じます。
何卒よろしくお願いいたします。
皆様お世話になっております。
選定に時間がかかりおまたせしております。
時期に決定となりますので、もうしばしお待ちくださいますようお願い申し上げます。

シンプルながら細部にこだわりがあり、明るいデザインに仕上げてくださいました。

皆様この度は作成くださりありがとうございました。
今後とも機会がございましたら何卒よろしくお願いいたします。

```html
<!DOCTYPE html>
<html lang="ja">
<head>
<meta charset="utf-8">
<title>Kelvado 学習塾</title>
<link href="https://fonts.googleapis.com/css2?family=Noto+Sans+JP:wght@400;500;700;900&family=Montserrat:wght@500;600;700&display=swap" rel="stylesheet">
<style>
:root{
  --green:#5cb82e;
  --green-dark:#2f4a2a;
  --green-light:#eef5ea;
  --ink:#333;
  --muted:#666;
  --dark:#2b2b2b;
  --white:#fff;
  --sakura:#f3dbe6;
}
*{box-sizing:border-box;margin:0;padding:0}
html,body{width:1200px;height:5208px;overflow:hidden}
body{font-family:"Noto Sans JP",sans-serif;color:var(--ink);background:var(--white);position:relative}
.en{font-family:"Montserrat","Noto Sans JP",sans-serif}
section,header,footer{position:absolute;left:0;width:1200px}
.ph{position:absolute}
.sec-title{text-align:center;color:var(--green);font-size:40px;font-weight:600;letter-spacing:2px}
.sec-title small{font-size:12px;margin-left:10px;font-weight:500}
.btn{display:flex;align-items:center;justify-content:center;gap:14px;background:var(--dark);color:#fff;font-size:16px;width:280px;height:56px;margin:0 auto;position:relative}
.btn::after{content:"";width:8px;height:8px;border-top:2px solid #fff;border-right:2px solid #fff;transform:rotate(45deg);position:absolute;right:22px}
.btn.green{background:var(--green)}

/* hero */
.hero{top:0;height:700px;background:linear-gradient(120deg,#dde6e2,#f4f6f5 45%,#c9d3d4)}
.hero .photo{left:0;top:0;width:1200px;height:600px;background:linear-gradient(110deg,#e9eeec 0%,#d7dfdc 40%,#4a5160 70%,#e5e9ea 100%)}
.hero .catch{position:absolute;left:0;top:240px;background:var(--green);color:#fff;font-size:44px;font-weight:700;padding:12px 36px 12px 40px;letter-spacing:2px}
.news{position:absolute;left:240px;top:480px;width:800px;height:108px;background:#fff;display:flex;align-items:center;padding:0 40px;gap:40px;box-shadow:0 2px 10px rgba(0,0,0,.06)}
.news h3{color:var(--green);font-size:20px;line-height:1.1}
.news h3 small{display:block;font-size:10px;font-weight:500}
.news ul{list-style:none;font-size:13px;flex:1}
.news li{padding:6px 0;border-bottom:1px solid #e3e3e3}
.news li span{color:var(--muted);margin-right:18px}
.news .more{font-size:12px;border-bottom:1px solid var(--ink)}

/* about */
.about{top:600px;height:560px;background:var(--green-light)}
.about .photo{left:0;top:60px;width:520px;height:420px;background:linear-gradient(135deg,#b9c0c8,#e6e2df 50%,#3d3f52)}
.about .head{position:absolute;right:80px;top:50px;color:var(--green);font-size:36px;font-weight:600;letter-spacing:3px}
.about .head small{font-size:12px;margin-right:12px;letter-spacing:0}
.about .lead{position:absolute;left:600px;top:120px;width:520px;color:var(--green);font-weight:700;font-size:17px}
.about .body{position:absolute;left:600px;top:170px;width:520px;font-size:12.5px;line-height:2;color:var(--muted)}
.about .btn{position:absolute;left:600px;top:420px;margin:0;width:230px;height:48px;font-size:14px}

/* classroom */
.classroom{top:1160px;height:760px}
.classroom .sec-title{margin-top:110px}
.rooms{display:flex;justify-content:center;gap:40px;margin-top:50px}
.room{width:260px;text-align:center}
.room .pic{width:260px;height:260px;border-radius:50%;background:linear-gradient(135deg,#c6ccd2,#f0ede8 55%,#8a8f98)}
.room p{margin-top:24px;font-size:15px;line-height:1.7}
.classroom .btn{margin-top:50px}

/* course */
.course{top:1920px;height:1020px;background:linear-gradient(#2c2c2c,#3a3a3a 70%,#4b4d48)}
.course .sec-title{color:#fff;margin-top:80px}
.course .sub{text-align:center;color:#fff;font-size:17px;font-weight:700;margin-top:20px}
.course .subs{text-align:center;color:#ccc;font-size:12px;margin-top:8px}
.cards{position:absolute;left:140px;top:270px;display:flex;gap:40px}
.card{width:440px}
.card .box{background:#fff;height:570px;padding-top:40px;text-align:center}
.card .pic{width:260px;height:260px;border-radius:50%;margin:0 auto;background:linear-gradient(135deg,#d6dfe6,#f3efe9 55%,#55607a)}
.card .tag{display:inline-block;background:var(--dark);color:#fff;font-size:14px;padding:10px 34px;margin-top:34px}
.card .desc{font-size:12.5px;line-height:1.9;color:var(--muted);margin:22px 40px 0;text-align:left}
.card .qa{background:var(--green);color:#fff;height:120px;display:flex;align-items:center;padding:0 36px;gap:18px;font-size:15px;font-weight:700;position:relative}
.card .qa b{font-family:"Montserrat",sans-serif;font-size:38px}
.card .qa::after{content:"";position:absolute;right:30px;width:10px;height:10px;border-top:2px solid #fff;border-right:2px solid #fff;transform:rotate(45deg)}

/* timetable */
.timetable{top:2940px;height:380px;background:var(--green-light);text-align:center}
.timetable h2{color:var(--green);font-size:28px;margin-top:90px}
.timetable p{font-size:13px;color:var(--muted);line-height:1.9;margin-top:14px}
.timetable .btn{margin-top:26px}

/* results */
.results{top:3320px;height:320px}
.results .photo{left:0;top:0;width:1200px;height:320px;background:linear-gradient(100deg,#f6e3ec,#fbf1f5 35%,#eaf2fb 55%,#f5dce8)}
.results h2{position:absolute;top:90px;width:100%;text-align:center;color:var(--green);font-size:22px}
.results .btns{position:absolute;top:200px;width:100%;display:flex;justify-content:center;gap:40px}
.results .btn{margin:0;width:250px}

/* teacher */
.teacher{top:3640px;height:640px;background:var(--green-dark)}
.teacher .sec-title{color:#fff;margin-top:80px}
.teachers{display:flex;justify-content:center;gap:60px;margin-top:40px}
.t{text-align:center;color:#fff;font-size:16px}
.t .pic{width:260px;height:260px;border-radius:50%;background:linear-gradient(135deg,#e8e8e8,#fafafa 50%,#9aa0a8);margin-bottom:22px}
.teacher .btn{margin-top:30px;width:270px;height:52px}

/* column */
.column{top:4300px;height:200px}
.column .box{position:absolute;left:200px;top:30px;width:800px;height:130px;background:#fff;box-shadow:0 2px 14px rgba(0,0,0,.1);display:flex;align-items:center;padding:0 40px;gap:40px}
.column h3{color:var(--green);font-size:22px;line-height:1.1}
.column h3 small{display:block;font-size:10px;font-weight:500}

/* inquiry */
.inquiry{top:4520px;height:300px;text-align:center}
.inquiry h2{color:var(--green);font-size:36px;margin-top:40px;letter-spacing:2px}
.inquiry .btns{display:flex;justify-content:center;gap:40px;margin-top:30px}
.inquiry a{display:flex;align-items:center;justify-content:center;gap:16px;width:400px;height:130px;background:var(--green);color:#fff;text-decoration:none;font-weight:700}
.inquiry .tel b{font-family:"Montserrat",sans-serif;font-size:36px;display:block}
.inquiry .tel small{font-size:13px}
.inquiry .form{font-size:28px}

/* footer */
.footer{top:4840px;height:368px;background:var(--green-light)}
.logo{position:absolute;left:60px;top:40px;display:flex;align-items:center;gap:10px;color:var(--green);font-size:34px;font-weight:900}
.logo i{width:26px;height:26px;background:var(--green);display:block}
.addr{position:absolute;left:60px;top:100px;font-size:12px;line-height:1.8;color:var(--muted)}
.links{position:absolute;left:420px;top:44px;display:flex;gap:50px;font-size:12px;line-height:2;list-style:none}
.links ul{list-style:none}
.map{left:820px;top:40px;width:340px;height:240px;background:linear-gradient(135deg,#e8eee6,#f5f3ee 50%,#dfe6ea)}
.copy{position:absolute;bottom:20px;width:100%;text-align:center;font-size:11px;color:var(--muted)}
</style>
</head>
<body>

<header class="hero">
  <div class="ph photo" role="img" aria-label="教室で学ぶ制服姿の女子生徒の写真"></div>
  <p class="catch">さあ、学力SWICH。</p>
  <div class="news">
    <h3 class="en">NEWS<small>新着情報</small></h3>
    <ul>
      <li><span>2022.08.01</span>夏期講習受付について</li>
      <li><span>2022.07.20</span>夏期講習受付について</li>
    </ul>
    <span class="more">新着情報一覧 →</span>
  </div>
</header>

<section class="about">
  <div class="ph photo" role="img" aria-label="教室で授業を受ける生徒たちの写真"></div>
  <h2 class="head en"><small>Kelvadoについて</small>ABOUT US</h2>
  <p class="lead">私たち人間にあって機械にないもの──それは「考える力」</p>
  <p class="body">これからの時代に求められるのは、自ら考え判断する力です。<br>Kelvadoでは一人ひとりの理解度に合わせた指導を行い、<br>「わかった」を積み重ねることで学ぶ楽しさを育てます。<br>少人数ならではの丁寧なサポートで目標達成まで伴走します。<br>講師と生徒が一緒に考える時間を何より大切にしています。<br>保護者の皆様とも密に連携し、安心して通える塾を目指します。</p>
  <a class="btn">Kelvadoについて</a>
</section>

<section class="classroom">
  <h2 class="sec-title en">CLASSROOM INTRODUCTION<small>教室紹介</small></h2>
  <div class="rooms">
    <div class="room"><div class="pic" role="img" aria-label="講師が授業をしている教室の写真"></div><p>講師がしっかりと見守し、<br>生徒をサポートします</p></div>
    <div class="room"><div class="pic" role="img" aria-label="教材が並ぶ本棚の写真"></div><p>教務教材が充実しています。<br>生徒の自習も可能です。</p></div>
    <div class="room"><div class="pic" role="img" aria-label="受付カウンターの写真"></div><p>開錠後以外は三ろ入り禁止。<br>セキュリティ面も安心です</p></div>
  </div>
  <a class="btn">教室紹介</a>
</section>

<section class="course">
  <h2 class="sec-title en">COURSE<small>コース紹介</small></h2>
  <p class="sub">第一志望合格とその先の自分らしい未来へ。</p>
  <p class="subs">それぞれの目標に合わせたコースをご用意し、一人ひとりに最適な指導を提供しています。</p>
  <div class="cards">
    <div class="card">
      <div class="box">
        <div class="pic" role="img" aria-label="授業で手を挙げる小学生の写真"></div>
        <span class="tag">中学受験をお考えの方 →</span>
        <p class="desc">ジュニアコース／中学受験コースでは基礎から応用まで段階的に力を伸ばし、志望校合格を目指します。</p>
      </div>
      <div class="qa"><b>Q&amp;A</b>よくあるご質問（小学生の方へ）</div>
    </div>
    <div class="card">
      <div class="box">
        <div class="pic" role="img" aria-label="ノートを持つ中学生の写真"></div>
        <span class="tag">高校受験をお考えの方 →</span>
        <p class="desc">ジュニアコース／中学部コースでは定期テスト対策と受験対策を両立し、確実な実力アップを図ります。</p>
      </div>
      <div class="qa"><b>Q&amp;A</b>よくあるご質問（中学生の方へ）</div>
    </div>
  </div>
</section>

<section class="timetable">
  <h2>時間割</h2>
  <p>小学生から中学生まで学年ごとの時間割をご確認いただけます。<br>季節講習の時間割は各講習の開始前に掲載いたします。</p>
  <a class="btn">時間割</a>
</section>

<section class="results">
  <div class="ph photo" role="img" aria-label="青空と満開の桜の写真"></div>
  <h2>合格実績＆体験記</h2>
  <div class="btns"><a class="btn">合格実績</a><a class="btn">合格体験記</a></div>
</section>

<section class="teacher">
  <h2 class="sec-title en">TEACHER<small>講師紹介</small></h2>
  <div class="teachers">
    <div class="t en"><div class="pic" role="img" aria-label="男性講師のポートレート写真"></div>Kenta Morishima</div>
    <div class="t en"><div class="pic" role="img" aria-label="男性講師のポートレート写真"></div>Ryosuke Tanabe</div>
    <div class="t en"><div class="pic" role="img" aria-label="女性講師のポートレート写真"></div>Mio Hasegawa</div>
  </div>
  <a class="btn green">講師紹介</a>
</section>

<section class="column">
  <div class="box">
    <h3 class="en">COLUMN<small>コラム</small></h3>
    <ul class="news" style="position:static;box-shadow:none;padding:0;height:auto;flex:1;display:block">
      <li><span>2022.08.01</span>やる気を高めるコツ</li>
      <li><span>2022.07.20</span>夏期講習受付について</li>
    </ul>
    <span class="news" style="position:static;box-shadow:none;padding:0;height:auto;width:auto;font-size:12px">コラム一覧 →</span>
  </div>
</section>

<section class="inquiry">
  <h2 class="en">INQUIRY</h2>
  <div class="btns">
    <a class="tel">
      <svg width="40" height="40" viewBox="0 0 24 24" fill="#fff"><path d="M6.6 10.8c1.4 2.8 3.8 5.1 6.6 6.6l2.2-2.2c.3-.3.7-.4 1-.2 1.1.4 2.3.6 3.6.6.6 0 1 .4 1 1V20c0 .6-.4 1-1 1C10.6 21 3 13.4 3 4c0-.6.4-1 1-1h3.5c.6 0 1 .4 1 1 0 1.3.2 2.5.6 3.6.1.3 0 .7-.2 1z"/></svg>
      <span><b>047-555-0192</b><small>（受付時間：9時〜22時）</small></span>
    </a>
    <a class="form">
      <svg width="40" height="30" viewBox="0 0 40 30" fill="none" stroke="#fff" stroke-width="3"><rect x="2" y="2" width="36" height="26"/><path d="M2 2l18 14L38 2"/></svg>
      問い合わせフォーム
    </a>
  </div>
</section>

<footer class="footer">
  <div class="logo en"><i></i>Kelvado</div>
  <p class="addr">〒270-0000 千葉県架空市緑町1-2-3<br>グリーンビル2F<br>TEL：047-555-0192</p>
  <div class="links">
    <ul><li>ホーム</li><li>Kelvadoについて</li><li>教室紹介</li><li>講師紹介</li><li>時間割</li><li>小学生の方へ</li><li>中学生の方へ</li></ul>
    <ul><li>中学受験をお考えの方</li><li>高校受験をお考えの方</li><li>合格実績</li><li>合格体験記</li><li>コラム</li><li>新着情報</li><li>お問い合わせ</li></ul>
  </div>
  <div class="ph map" role="img" aria-label="教室周辺の地図"></div>
  <p class="copy">© Kelvado All Rights Reserved.</p>
</footer>

</body>
</html>
```